Webdesign für Planung, Beratung, Service, Gutachten, Wartung und Verkauf von PV-Anlagen
Zielgruppe
Domainname: KWB720 steht für Lichtweg Energieberatung
Planung, Beratung, Service, Gutachten, Wartung und Verkauf von PV Anlagen. Der Fokus liegt hier aber mehr auf Qualität statt Quantität. Die unabhängige Beratung ohne Verkaufsabsicht steht im Vordergrund.
Aufgabenstellung
Vertrauen und Emotionen möchte ich übertragen. Das Persönliche soll rüberkommen.

```html
<!DOCTYPE html>
<html lang="de">
<head>
<meta charset="utf-8">
<title>Lichtweg Energieberatung – Photovoltaik</title>
<link rel="stylesheet" href="https://fonts.googleapis.com/css2?family=Jost:wght@400;500;600&display=swap">
<style>
  :root {
    --bg: #181829;
    --bg-deep: #141424;
    --text: #ffffff;
    --muted: #a9a9bd;
    --nav-text: #c9c9d6;
    --card-bg: rgba(255, 255, 255, 0.055);
    --card-border: rgba(255, 255, 255, 0.13);
    --accent: #3a7bc4;
    --icon-frame: #d6d6e2;
    --icon-pen: #f07a1d;
    --line: rgba(255, 255, 255, 0.35);
  }
  * { margin: 0; padding: 0; box-sizing: border-box; }
  html, body { width: 1200px; height: 675px; overflow: hidden; }
  body {
    position: relative;
    background: var(--bg);
    font-family: "Jost", sans-serif;
    color: var(--text);
  }
  .panel-backdrop {
    position: absolute; inset: 86px 0 0 0;
    background:
      radial-gradient(ellipse 520px 300px at 120px 600px, rgba(70,70,100,0.35), transparent 70%),
      radial-gradient(ellipse 560px 360px at 1100px 560px, rgba(80,80,110,0.35), transparent 70%),
      linear-gradient(180deg, var(--bg-deep) 0%, var(--bg) 45%, #25253a 100%);
  }
  .site-header {
    position: absolute; top: 0; left: 0; width: 1200px; height: 86px;
    border-bottom: 1px solid rgba(255,255,255,0.05);
    background: var(--bg-deep);
  }
  .brand {
    position: absolute; left: 180px; top: 35px;
    display: flex; align-items: center; gap: 8px;
    font-size: 12px; font-weight: 500;
    color: var(--nav-text);
  }
  .brand-dot { width: 9px; height: 9px; border-radius: 50%; background: var(--accent); }
  .main-nav a {
    position: absolute; top: 38px;
    font-size: 9.6px; color: var(--nav-text); text-decoration: none;
  }
  .cta {
    position: absolute; left: 888px; top: 29px; width: 121px; height: 25px;
    border-radius: 13px; background: var(--accent);
    font-size: 8.3px; color: #fff; display: flex; align-items: center; justify-content: center;
  }
  .hero-title {
    position: absolute; top: 136px; left: 0; width: 1200px;
    text-align: center; font-weight: 600; font-size: 38px; line-height: 41px;
  }
  .hero-lead {
    position: absolute; top: 232px; left: 326px; width: 548px;
    text-align: center; font-size: 11.2px; line-height: 17.5px; color: var(--muted);
  }
  .connectors { position: absolute; left: 0; top: 0; }
  .core-visual {
    position: absolute; left: 497px; top: 354px; width: 206px; height: 206px;
    border-radius: 50%;
    background: radial-gradient(circle, #1b1b30 55%, rgba(58,123,196,0.28) 75%, rgba(240,122,29,0.18) 88%, transparent 100%);
  }
  .service-card {
    position: absolute; width: 292px; height: 64px;
    background: var(--card-bg); border: 1px solid var(--card-border); border-radius: 3px;
  }
  .service-card svg { position: absolute; left: 17px; top: 17px; }
  .service-card h3 {
    position: absolute; left: 51px; top: 15px;
    font-size: 11.5px; font-weight: 500; color: #e8e8f0;
  }
  .service-card p {
    position: absolute; left: 51px; top: 35px;
    font-size: 10.3px; color: #c4c4d2; white-space: nowrap;
  }
</style>
</head>
<body>
  <div class="panel-backdrop" role="img" aria-label="Dezentes Foto von Solarmodulen im Hintergrund"></div>

  <header class="site-header">
    <div class="brand"><span class="brand-dot"></span>Lichtweg Energieberatung</div>
    <nav class="main-nav">
      <a href="#" style="left:469px">Startseite</a>
      <a href="#" style="left:550px">Über uns</a>
      <a href="#" style="left:631px">Portfolio</a>
      <a href="#" style="left:707px">Blog</a>
      <a href="#" style="left:769px">Kontakt</a>
    </nav>
    <a class="cta">Unverbindliche Beratung</a>
  </header>

  <h1 class="hero-title">Machen Sie sich unabhängiger<br>nutzen Sie Sonnenenergie</h1>
  <p class="hero-lead">Lorem ipsum dolor sit amet consetetur sadipscing elitr sed diam nonumy eirmod tempor invidunt ut labore et dolore magna aliquyam sed diam voluptua. At vero eos et accusam et justo duo dolores et ea rebum.</p>

  <div class="core-visual" role="img" aria-label="Zentrale Grafik der Leistungsbereiche"></div>

  <svg class="connectors" width="1200" height="675" viewBox="0 0 1200 675">
    <g fill="none" stroke="var(--line)" stroke-width="0.8" stroke-dasharray="1.5 1.5">
      <polyline points="457,353 491,353 530,402"/>
      <polyline points="426,456 510,456"/>
      <polyline points="457,562 491,562 530,514"/>
      <polyline points="746,357 712,357 673,405"/>
      <polyline points="777,456 703,456"/>
      <polyline points="746,559 712,559 673,511"/>
    </g>
    <g fill="#ffffff" stroke="rgba(255,255,255,0.35)" stroke-width="2">
      <circle cx="530" cy="402" r="4"/>
      <circle cx="510" cy="456" r="4"/>
      <circle cx="530" cy="514" r="4"/>
      <circle cx="673" cy="405" r="4"/>
      <circle cx="703" cy="456" r="4"/>
      <circle cx="673" cy="511" r="4"/>
    </g>
  </svg>

  <svg width="0" height="0" style="position:absolute">
    <symbol id="icon-edit" viewBox="0 0 24 24">
      <path d="M11 4H4.5a1 1 0 0 0-1 1v14.5a1 1 0 0 0 1 1H19a1 1 0 0 0 1-1V13" fill="none" stroke="var(--icon-frame)" stroke-width="1.4" stroke-linecap="round"/>
      <path d="M18.5 2.5l3 3L12 15l-4 1 1-4z" fill="none" stroke="var(--icon-pen)" stroke-width="1.4" stroke-linejoin="round"/>
    </symbol>
  </svg>

  <article class="service-card" style="left:165px;top:328px">
    <svg width="22" height="22"><use href="#icon-edit"/></svg>
    <h3>Planung</h3><p>Lorem ipsum dolor sit amet consetetur sadipscing</p>
  </article>
  <article class="service-card" style="left:134px;top:424px">
    <svg width="22" height="22"><use href="#icon-edit"/></svg>
    <h3>Beratung</h3><p>Lorem ipsum dolor sit amet consetetur sadipscing</p>
  </article>
  <article class="service-card" style="left:165px;top:520px">
    <svg width="22" height="22"><use href="#icon-edit"/></svg>
    <h3>Service</h3><p>Lorem ipsum dolor sit amet consetetur sadipscing</p>
  </article>
  <article class="service-card" style="left:746px;top:328px">
    <svg width="22" height="22"><use href="#icon-edit"/></svg>
    <h3>Gutachten</h3><p>Lorem ipsum dolor sit amet consetetur sadipscing</p>
  </article>
  <article class="service-card" style="left:777px;top:424px">
    <svg width="22" height="22"><use href="#icon-edit"/></svg>
    <h3>Wartung</h3><p>Lorem ipsum dolor sit amet consetetur sadipscing</p>
  </article>
  <article class="service-card" style="left:746px;top:520px">
    <svg width="22" height="22"><use href="#icon-edit"/></svg>
    <h3>Verkauf</h3><p>Lorem ipsum dolor sit amet consetetur sadipscing</p>
  </article>
</body>
</html>
```